"Inkvale" printing shop

-The design must be based around the attached Print House (home page information design) called "Inkvale - HPID".

The table boxes are just for approximate placement of information – you DON'T have to box everything in and you can arrange these. All fonts used in the Print House are only examples - you can use any Google font you wish.

- Information only is in orange text. Copy to go on the design in black text. Some instructions are in the Print House. Please be creative!

-The design needs to be modern. Colours are to be consistent with their new logo or complement it. Keep it clean and simple, you don't need to use lots of colours. Use lots of white.

- images / icons for the site need to be relevant and high quality, but they must also be free images or icons. I have attached a few examples that could be used.

Width of content will be 1100 pixels when implemented as a web page. Header height (without nav bar) 150-200 pixels.

If your design is chosen the winning PSD file will have to be provided as follows…
1. Canvas size of 2000px x 2000px - 72ppi in Adobe Photoshop (CS5 compatible)
2. Width of content section is 1100px wide - centered in the canvas
3. Any button rollovers/hovers in the PSD as hidden layers.
4. All fonts used must be Google fonts.
5. You will need to supply the chosen home page plus one example page (example page as a style guide for how all other pages will look). Example page is only the header and navigational bar at the top, an empty sector in the middle with a column (190 px wide) which can be left or right aligned which means the main sector is 910 pixels wide, and then the footer at the bottom of the page

Checklist - http://layoutreviewlist.example/

Examples of some websites that have great design... don't copy them please but they are similar in look to what we are after....
http://www.pawnriverhub.example/

Industry/Entity Type

Printing

Font styles to use
Serif
Sans Serif

Requirements
Should not have
• Drop shadows, comic sans font

```html
<!DOCTYPE html>
<html lang="en">
<head>
<meta charset="utf-8">
<title>Inkvale – Printing Shop</title>
<link href="https://fonts.googleapis.com/css2?family=Lato:wght@300;400;700&display=swap" rel="stylesheet">
<style>
:root{
  --pink:#d93f7e;
  --ink:#3a3a3a;
  --text:#444;
  --grey-bg:#efefef;
  --rule:#e2e2e2;
  --dark:#414141;
  --darker:#333;
  --white:#fff;
}
*{box-sizing:border-box;margin:0;padding:0}
html,body{width:1200px;height:2275px;overflow:hidden}
body{font-family:'Lato',sans-serif;color:var(--text);background:var(--white)}
.wrap{width:952px;margin:0 auto;position:relative}

/* top bar */
.topbar{height:40px;border-bottom:1px solid var(--rule)}
.topbar .wrap{display:flex;justify-content:space-between;align-items:center;height:40px;font-size:12px;color:var(--pink)}
.topbar nav a{color:var(--pink);text-decoration:none;text-transform:uppercase;margin-left:22px}
.topbar nav span{margin-left:22px;color:var(--pink)}

/* header */
.masthead{height:137px;border-bottom:1px solid var(--rule)}
.masthead .wrap{display:flex;align-items:center;height:137px}
.brand{display:flex;align-items:center;gap:10px;width:199px;flex:none}
.brand-dot{width:40px;height:40px;border-radius:50%;background:var(--pink)}
.brand-name{font-size:36px;font-weight:700;color:var(--pink)}
.tagline h1{font-weight:400;font-size:35px;letter-spacing:3px;color:var(--ink)}
.tagline p{font-size:16px;color:var(--ink);margin-top:4px;font-weight:300}
.contact{margin-left:auto;width:150px;flex:none;font-size:13.5px;color:var(--ink);line-height:1.45}
.contact div{display:flex;gap:8px;align-items:flex-start;margin-bottom:12px}
.contact svg{flex:none;margin-top:3px}

/* services nav */
.services-nav{height:84px;border-bottom:1px solid var(--rule)}
.services-nav .wrap{display:flex;align-items:center;height:84px;font-size:12px;color:var(--pink);justify-content:space-between}
.services-nav a{color:var(--pink);text-decoration:none}

/* hero */
.hero{height:393px;border-bottom:1px solid var(--rule)}
.hero .wrap{height:393px}
.hero h2{position:absolute;left:0;top:85px;font-weight:400;font-size:32px;line-height:41px;color:var(--ink);width:440px}
.btn-pill{position:absolute;left:0;top:247px;width:136px;height:43px;border-radius:22px;background:var(--pink);color:var(--white);font-size:14px;display:flex;align-items:center;justify-content:center;gap:6px;text-transform:uppercase}
.hero-visual{position:absolute;left:490px;top:31px;width:437px;height:362px;background:linear-gradient(160deg,#3a3d44 0%,#1f2126 55%,#d9dadc 100%);border-radius:6px 6px 0 0}

/* service cards */
.services{height:685px;background:var(--grey-bg);padding-top:46px}
.card-grid{display:grid;grid-template-columns:repeat(3,301px);column-gap:24.5px;row-gap:26px}
.card{height:285px;background:var(--white);border-radius:8px;overflow:hidden;position:relative}
.card-top{height:105px;background:var(--pink);display:flex;justify-content:center;padding-top:18px}
.card-body{position:absolute;top:96px;left:0;right:0;bottom:0;background:var(--white);border-radius:12px 12px 0 0;padding:30px 32px 0 17px}
.card h3{font-size:21px;font-weight:700;color:var(--pink);margin-bottom:10px}
.card p{font-size:11.5px;line-height:14px;color:var(--text)}
.btn-more{display:flex;margin-top:16px;width:110px;height:40px;border-radius:6px;overflow:hidden}
.btn-more span{flex:1;background:var(--pink);color:var(--white);font-weight:700;font-size:14px;display:flex;align-items:center;justify-content:center}
.btn-more i{width:42px;background:var(--ink);display:flex;align-items:center;justify-content:center}

/* numbered features */
.features{height:405px;padding-top:40px}
.feature-grid{display:grid;grid-template-columns:465px 465px;column-gap:22px}
.feature{display:flex;gap:14px;height:118px;padding-top:2px}
.feature-num{flex:none;width:58px;height:58px;border-radius:50%;background:var(--pink);color:var(--white);font-size:32px;display:flex;align-items:center;justify-content:center}
.feature-body{flex:1;border-bottom:1px solid var(--rule);height:87px}
.feature h4{font-size:17.5px;font-weight:700;color:var(--pink);margin-bottom:6px}
.feature p{font-size:11.2px;line-height:14px;color:var(--darker)}
.more-info{display:flex;align-items:center;gap:6px;font-size:14px;font-weight:700;color:var(--pink);margin-top:3px}

/* quote */
.quote{height:410px;background:var(--dark);color:var(--white)}
.quote .wrap{display:flex;height:410px;padding-top:34px}
.quote-intro{width:405px}
.quote h3{font-size:24px;font-weight:700;margin-bottom:28px}
.quote-intro p{font-size:17px;line-height:20px;margin-bottom:18px;padding-right:20px;font-weight:300}
.social{display:flex;gap:21px;margin-top:44px}
.social span{width:47px;height:47px;border-radius:50%;background:var(--pink)}
.quote-form{width:547px}
.field-row{display:flex;gap:11px;margin-bottom:9px}
.field{flex:1;height:34px;border:1px solid #cfcfcf;font-size:12px;padding:9px;color:var(--white)}
.field.message{height:90px;flex:none;width:100%}
.btn-send{margin:8px auto 0;width:105px;height:33px;border-radius:8px;background:var(--pink);color:var(--white);font-size:13px;font-weight:700;font-style:normal;display:flex;align-items:center;justify-content:center}

/* footer */
.footer-nav{height:62px;background:var(--pink)}
.footer-nav .wrap{display:flex;align-items:center;height:62px;justify-content:space-between;font-size:10.5px;color:var(--white)}
.footer-nav a{color:var(--white);text-decoration:none}
.legal{height:59px;background:var(--darker);display:flex;align-items:center;justify-content:center;font-size:13px;color:#aaa}
</style>
</head>
<body>

<header class="topbar">
  <div class="wrap">
    <span>Wel come to our site...!</span>
    <nav><a href="#">Home</a><span>|</span><a href="#">About us</a><span>|</span><a href="#">Contct</a><span>|</span><a href="#">Free quote</a></nav>
  </div>
</header>

<section class="masthead">
  <div class="wrap">
    <div class="brand"><span class="brand-dot"></span><span class="brand-name">Inkvale</span></div>
    <div class="tagline">
      <h1>Duplication is our vocation</h1>
      <p>Professional photocopying - digital &amp; film processing, design and printing</p>
    </div>
    <div class="contact">
      <div><svg width="12" height="13" viewBox="0 0 24 24"><path fill="#444" d="M6.6 10.8a15.1 15.1 0 006.6 6.6l2.2-2.2a1 1 0 011-.25 11.4 11.4 0 003.6.57 1 1 0 011 1V20a1 1 0 01-1 1A17 17 0 013 4a1 1 0 011-1h3.5a1 1 0 011 1c0 1.25.2 2.45.57 3.57a1 1 0 01-.25 1z"/></svg><span>07 555 0186</span></div>
      <div><svg width="10" height="14" viewBox="0 0 10 14"><path fill="#444" d="M5 0a5 5 0 00-5 5c0 3.7 5 9 5 9s5-5.3 5-9a5 5 0 00-5-5zm0 7a2 2 0 110-4 2 2 0 010 4z"/></svg><span>12/48 Harbour Road<br>Harbour - Tauranga</span></div>
    </div>
  </div>
</section>

<nav class="services-nav">
  <div class="wrap">
    <a href="#">Photocopying</a>|<a href="#">Printing</a>|<a href="#">Laminating</a>|<a href="#">Business cards</a>|<a href="#">Typing services</a>|<a href="#">Film processing</a>|<a href="#">Photo Printing</a>|<a href="#">Passport photos</a>|<a href="#">Image Restoration</a>|<a href="#">Printer Supplies</a>
  </div>
</nav>

<section class="hero">
  <div class="wrap">
    <h2>Digital printing Laminating Photocopying Services Throughout Tauranga</h2>
    <a class="btn-pill">Read more <svg width="13" height="13" viewBox="0 0 14 14"><circle cx="7" cy="7" r="7" fill="#fff"/><path d="M6 4l3 3-3 3" stroke="#d93f7e" stroke-width="2" fill="none"/></svg></a>
    <div class="hero-visual" role="img" aria-label="Photo of a large office multifunction copier printing a document"></div>
  </div>
</section>

<section class="services">
  <div class="wrap card-grid">
    <article class="card">
      <div class="card-top"><svg width="80" height="64" viewBox="0 0 80 64" fill="none" stroke="#fff" stroke-width="4" stroke-linejoin="round"><path d="M40 6L74 22 40 38 6 22z"/><path d="M6 32l34 16 34-16"/><path d="M6 42l34 16 34-16"/></svg></div>
      <div class="card-body"><h3>Photocopying</h3><p>Ex ea commodo consequat. Duis aute irure dolor in reprehenderie ctetur adipisicing elit sed iusmod tempor incididunt ut lab.</p><a class="btn-more"><span>MORE</span><i><svg width="18" height="18" viewBox="0 0 14 14"><circle cx="7" cy="7" r="7" fill="#fff"/><path d="M6 4l3 3-3 3" stroke="#3a3a3a" stroke-width="2" fill="none"/></svg></i></a></div>
    </article>
    <article class="card">
      <div class="card-top"><svg width="64" height="62" viewBox="0 0 64 62" fill="none" stroke="#fff" stroke-width="4" stroke-linejoin="round"><path d="M4 16L54 4"/><rect x="8" y="20" width="44" height="18"/><path d="M16 38v20h24V38"/><path d="M56 22h4M56 30h4"/></svg></div>
      <div class="card-body"><h3>Laminating &amp; Binding</h3><p>Ex ea commodo consequat. Duis aute irure dolor in reprehenderie ctetur adipisicing elit sed iusmod tempor incididunt ut lab.</p><a class="btn-more"><span>MORE</span><i><svg width="18" height="18" viewBox="0 0 14 14"><circle cx="7" cy="7" r="7" fill="#fff"/><path d="M6 4l3 3-3 3" stroke="#3a3a3a" stroke-width="2" fill="none"/></svg></i></a></div>
    </article>
    <article class="card">
      <div class="card-top"><svg width="60" height="60" viewBox="0 0 60 60" fill="none" stroke="#fff" stroke-width="4" stroke-linejoin="round"><rect x="16" y="4" width="28" height="18"/><path d="M22 11h16M22 16h16" stroke-width="3"/><rect x="4" y="24" width="52" height="22" rx="3" fill="#fff"/><rect x="14" y="42" width="32" height="14" fill="#d93f7e"/></svg></div>
      <div class="card-body"><h3>Digital Printing</h3><p>Ex ea commodo consequat. Duis aute irure dolor in reprehenderie ctetur adipisicing elit sed iusmod tempor incididunt ut lab.</p><a class="btn-more"><span>MORE</span><i><svg width="18" height="18" viewBox="0 0 14 14"><circle cx="7" cy="7" r="7" fill="#fff"/><path d="M6 4l3 3-3 3" stroke="#3a3a3a" stroke-width="2" fill="none"/></svg></i></a></div>
    </article>
    <article class="card">
      <div class="card-top"><svg width="64" height="64" viewBox="0 0 64 64"><circle cx="32" cy="32" r="30" fill="#fff"/><circle cx="32" cy="32" r="6" fill="#d93f7e"/><path d="M28 6h8v16h-8zM10 44l14-8 4 7-14 8zM54 44l-14-8-4 7 14 8z" fill="#d93f7e"/></svg></div>
      <div class="card-body"><h3>Film Processing</h3><p>Ex ea commodo consequat. Duis aute irure dolor in reprehenderie ctetur adipisicing elit sed iusmod tempor incididunt ut lab.</p><a class="btn-more"><span>MORE</span><i><svg width="18" height="18" viewBox="0 0 14 14"><circle cx="7" cy="7" r="7" fill="#fff"/><path d="M6 4l3 3-3 3" stroke="#3a3a3a" stroke-width="2" fill="none"/></svg></i></a></div>
    </article>
    <article class="card">
      <div class="card-top"><svg width="72" height="52" viewBox="0 0 72 52" fill="none" stroke="#fff" stroke-width="4"><rect x="3" y="3" width="66" height="46" rx="6"/><rect x="14" y="16" width="18" height="18" fill="#fff"/><path d="M40 18h18M40 26h18M40 34h12"/></svg></div>
      <div class="card-body"><h3>Business Cards</h3><p>Ex ea commodo consequat. Duis aute irure dolor in reprehenderie ctetur adipisicing elit sed iusmod tempor incididunt ut lab.</p><a class="btn-more"><span>MORE</span><i><svg width="18" height="18" viewBox="0 0 14 14"><circle cx="7" cy="7" r="7" fill="#fff"/><path d="M6 4l3 3-3 3" stroke="#3a3a3a" stroke-width="2" fill="none"/></svg></i></a></div>
    </article>
    <article class="card">
      <div class="card-top"><svg width="66" height="62" viewBox="0 0 66 62" fill="none" stroke="#fff" stroke-width="3.5" stroke-linejoin="round"><rect x="4" y="10" width="44" height="20" rx="4"/><path d="M14 4h28v6"/><rect x="20" y="24" width="42" height="20" rx="4" fill="#fff"/><path d="M26 44v14h24l6-6V44"/><path d="M32 50h14"/></svg></div>
      <div class="card-body"><h3>Photo Printing</h3><p>Ex ea commodo consequat. Duis aute irure dolor in reprehenderie ctetur adipisicing elit sed iusmod tempor incididunt ut lab.</p><a class="btn-more"><span>MORE</span><i><svg width="18" height="18" viewBox="0 0 14 14"><circle cx="7" cy="7" r="7" fill="#fff"/><path d="M6 4l3 3-3 3" stroke="#3a3a3a" stroke-width="2" fill="none"/></svg></i></a></div>
    </article>
  </div>
</section>

<section class="features">
  <div class="wrap feature-grid">
    <div class="feature"><span class="feature-num">1</span><div class="feature-body"><h4>Cost effective photocopying</h4><p>No matter the quantity of photocopies you need or the size of your copy - you can rely on us to provide a top quality service!</p><span class="more-info">MORE INFO <svg width="13" height="11" viewBox="0 0 13 11"><path d="M8 0l5 4.5L8 9V6C4 6 2 7 0 11c0-5 3-8 8-8z" fill="#d93f7e"/></svg></span></div></div>
    <div class="feature"><span class="feature-num">2</span><div class="feature-body"><h4>Personal desktop publishing</h4><p>From personalised brochures, posters and birthday and special occasion cards to top quality, cheap business cards - you get it all!</p><span class="more-info">MORE INFO <svg width="13" height="11" viewBox="0 0 13 11"><path d="M8 0l5 4.5L8 9V6C4 6 2 7 0 11c0-5 3-8 8-8z" fill="#d93f7e"/></svg></span></div></div>
    <div class="feature"><span class="feature-num">3</span><div class="feature-body"><h4>All digital format printing</h4><p>Either email us your file or bring it into the store and we can get you the print you need. All prints are to the highest quality.</p><span class="more-info">MORE INFO <svg width="13" height="11" viewBox="0 0 13 11"><path d="M8 0l5 4.5L8 9V6C4 6 2 7 0 11c0-5 3-8 8-8z" fill="#d93f7e"/></svg></span></div></div>
    <div class="feature"><span class="feature-num">4</span><div class="feature-body"><h4>Film photo processing</h4><p>Bring in your film to the store and we will work with you to get the best quality print for your purpose and needs. We work with it all!</p><span class="more-info">MORE INFO <svg width="13" height="11" viewBox="0 0 13 11"><path d="M8 0l5 4.5L8 9V6C4 6 2 7 0 11c0-5 3-8 8-8z" fill="#d93f7e"/></svg></span></div></div>
    <div class="feature"><span class="feature-num">5</span><div class="feature-body"><h4>Laminating and binding</h4><p>Create a professional image for your documents or books. Lamination and binding also keeps your documents well protected!</p><span class="more-info">MORE INFO <svg width="13" height="11" viewBox="0 0 13 11"><path d="M8 0l5 4.5L8 9V6C4 6 2 7 0 11c0-5 3-8 8-8z" fill="#d93f7e"/></svg></span></div></div>
    <div class="feature"><span class="feature-num">6</span><div class="feature-body"><h4>Quality digital photo prints</h4><p>Get your photo printed to your requirements - either from a file or from your digital camera. With a wide range of options you can get the print you want.</p><span class="more-info">MORE INFO <svg width="13" height="11" viewBox="0 0 13 11"><path d="M8 0l5 4.5L8 9V6C4 6 2 7 0 11c0-5 3-8 8-8z" fill="#d93f7e"/></svg></span></div></div>
  </div>
</section>

<section class="quote">
  <div class="wrap">
    <div class="quote-intro">
      <h3>Get a free quote</h3>
      <p>...or talk to our team about your requirements. Please fill out the form below and we will contact you within a day.</p>
      <p>You can now upload and send us your file for a free quote!</p>
      <div class="social" aria-label="Social links"><span></span><span></span><span></span><span></span><span></span><span></span></div>
    </div>
    <form class="quote-form">
      <h3>Equire Form</h3>
      <div class="field-row"><div class="field">First Name</div><div class="field">Last Name</div></div>
      <div class="field-row"><div class="field">Number</div><div class="field">Email</div></div>
      <div class="field-row"><div class="field message">Message</div></div>
      <i class="btn-send">SEND</i>
    </form>
  </div>
</section>

<nav class="footer-nav">
  <div class="wrap">
    <a href="#">Home</a>|<a href="#">About</a>|<a href="#">Photocopying</a>|<a href="#">Printing</a>|<a href="#">Laminating</a>|<a href="#">Business cards</a>|<a href="#">Typing services</a>|<a href="#">Film processing</a>|<a href="#">Photo Printing</a>|<a href="#">Passport photos</a>|<a href="#">Image Restoration</a>|<a href="#">Printer Supplies</a>|<a href="#">Free quote</a>|<a href="#">Contact</a>
  </div>
</nav>

<footer class="legal">Inkvale - Print House © copyright 2015 • Privacy Policy</footer>

</body>
</html>
```